The Orchard Gate

The Design Brief and Flyer Text are in Documents attached
Other design components also attached
Only allowed five doc attachments - so please use the first pic of sculpture for the remaining three and then once design is finalised I can send you the other pics for the print ready files
Many thanks
Tom Harland
tom@velmora4.com
01632 480517

```html
<!DOCTYPE html>
<html lang="en">
<head>
<meta charset="utf-8">
<title>The Inner Return – Leaflet</title>
<link href="https://fonts.googleapis.com/css2?family=PT+Sans:wght@400;700&family=Didact+Gothic&display=swap" rel="stylesheet">
<style>
:root{
  --stage:#5f656b;
  --paper:#f6f1dc;
  --wine:#8c1a2a;
  --bronze:#8a5a2a;
  --ink:#1f1f1f;
  --leaf:#5d9a2e;
  --lime:#b7dc4a;
  --rule:#8a8a80;
  --white:#ffffff;
}
*{margin:0;padding:0;box-sizing:border-box}
html,body{width:837px;height:1200px;overflow:hidden;background:var(--stage)}
body{position:relative;font-family:"Didact Gothic",sans-serif;color:var(--ink)}
.sheet{position:absolute;background:var(--paper);overflow:hidden}
.sheet--front{left:18px;top:25px;width:800px;height:565px}
.sheet--inside{left:18px;top:613px;width:800px;height:561px}
.fold{position:absolute;left:400px;top:0;width:1px;height:100%;background:#b9b39a}
.vine{position:absolute;border-radius:50%;background:radial-gradient(ellipse at center,rgba(93,154,46,.5),rgba(169,207,122,.22) 60%,rgba(246,241,220,0) 75%)}
.programme{font-family:"PT Sans",sans-serif;font-weight:700;color:var(--wine)}

/* front: instructions panel */
.panel-title{position:absolute;left:0;top:52px;width:400px;text-align:center;font-size:30px;line-height:32px}
.tagline{position:absolute;left:0;top:128px;width:400px;text-align:center;font-size:9.5px;letter-spacing:.5px}
.stage-head{position:absolute;left:74px;font-family:"PT Sans",sans-serif;font-weight:700;font-size:10.5px;color:var(--bronze)}
.stage-head::before{content:"";position:absolute;left:-15px;top:2px;width:10px;height:10px;border-radius:50% 0;background:var(--leaf)}
.steps{position:absolute;left:74px;width:295px;list-style:none;font-size:10px;line-height:11.5px}
.steps li{position:relative;padding-left:18px;margin-bottom:9.5px}
.steps li::before{content:"•";position:absolute;left:3px}
.org{position:absolute;left:0;top:484px;width:400px;text-align:center}
.org .name{font-family:"PT Sans",sans-serif;font-size:13px;color:var(--wine)}
.org .sub{font-size:9.5px;letter-spacing:1px;margin-top:3px}
.credits{position:absolute;left:0;top:524px;width:400px;text-align:center;font-size:7px;line-height:8.5px}

/* front: cover */
.cover-art{position:absolute;left:434px;top:42px;width:350px;height:402px;border-radius:175px 175px 40px 40px;background:linear-gradient(180deg,#cfe3b4 0%,#6f9a4b 40%,#4a6e32 70%,#e8e6dc 78%,#2a2a2a 88%,#f6f1dc 100%)}
.cover-title{position:absolute;left:434px;top:236px;width:350px;text-align:center;font-size:34px;line-height:36px;color:var(--white)}
.cover-band{position:absolute;left:400px;top:430px;width:400px;height:135px;background:linear-gradient(180deg,rgba(246,241,220,0) 0%,#dcebaa 30%,var(--lime) 100%)}
.cover-name{position:absolute;left:400px;top:476px;width:400px;text-align:center;font-family:"PT Sans",sans-serif;font-weight:700;font-size:23px;color:var(--wine)}
.cover-sub{position:absolute;left:400px;top:505px;width:400px;text-align:center;font-size:9.5px;letter-spacing:1px}
.cover-note{position:absolute;left:400px;top:521px;width:400px;text-align:center;font-size:10px;line-height:12px}

/* inside */
.swoosh{position:absolute;left:290px;top:50px;width:200px;height:46px;border-radius:50%;background:linear-gradient(90deg,rgba(150,120,220,.5),rgba(240,160,60,.6),rgba(250,230,90,.5));filter:blur(6px)}
.inside-title{position:absolute;left:0;top:80px;width:800px;text-align:center;font-size:30px;line-height:34px}
.copy{font-size:7.8px;line-height:11.2px}
.intro{position:absolute;left:48px;top:138px;width:696px;text-align:justify}
.lead{position:absolute;left:48px;top:195px;width:300px}
.entry{position:absolute}
.entry h3{font-family:"PT Sans",sans-serif;font-weight:700;font-size:9.5px;line-height:11px}
.entry .motto{font-weight:700}
.entry p{text-align:justify}
.rule{position:absolute;height:1px;background:var(--rule)}
.sculpture{position:absolute;width:58px;background:linear-gradient(180deg,#dbe8c6 0%,#8fb46a 35%,#c9cbc4 55%,#6e8a4c 100%)}
.sculpture.dark{background:linear-gradient(180deg,#b9d3e6 0%,#6f8fa6 30%,#2c3038 50%,#4f6f3a 100%)}
</style>
</head>
<body>

<section class="sheet sheet--front">
  <div class="fold"></div>
  <div class="vine" role="img" aria-label="Trailing ivy vine with red berries" style="left:10px;top:20px;width:150px;height:80px"></div>
  <div class="vine" role="img" aria-label="Trailing ivy vine with red berries" style="left:270px;top:20px;width:140px;height:70px"></div>

  <div class="programme panel-title">The Inner<br>Return</div>
  <div class="tagline">A SILENT journey in three stages</div>

  <div class="stage-head" style="top:154px">The Journey Inward</div>
  <ul class="steps" style="top:176px">
    <li>Walk slowly to the centre - at least half the pace you normally walk</li>
    <li>Stop for a few moments at each of the six stone sculptures</li>
    <li>Contemplate what each one means to you - see what it awakens within you</li>
  </ul>

  <div class="stage-head" style="top:270px">At the Centre</div>
  <ul class="steps" style="top:292px">
    <li>Stop and just be in complete silence</li>
    <li>Meditate on I AM</li>
    <li>Be silent - be still - just be the ‘I’ that says, “I am”.</li>
  </ul>

  <div class="stage-head" style="top:365px">The Journey Outwards</div>
  <ul class="steps" style="top:386px">
    <li>As you return you take the same path at the same pace but you now feel different</li>
    <li>You return to the world with a new state of being</li>
    <li>As you walk visualise what you might do differently when you arrive back in the world of action and interaction!</li>
  </ul>

  <div class="org">
    <div class="name">Calm in the Meadow</div>
    <div class="sub">HILLSIDE RETREAT HOUSE</div>
  </div>
  <div class="credits">The Orchard Gate Designed and Created by - Owen Pritchard<br>Sculptures Created by - Lars Vennick</div>

  <div class="cover-art" role="img" aria-label="Garden archway of climbing ivy framing a tree-lined path, above a circular walking-meditation path drawing"></div>
  <div class="programme cover-title">The Inner<br>Return</div>
  <div class="cover-band"></div>
  <div class="cover-name">The Orchard Gate</div>
  <div class="cover-sub">SILENT WALKING MEDITATION</div>
  <div class="cover-note">Don’t forget to walk The Orchard Gate<br>and rediscover your SELF at the top of the gardens</div>
</section>

<section class="sheet sheet--inside">
  <div class="vine" role="img" aria-label="Trailing ivy vine with red berries" style="left:0;top:10px;width:300px;height:70px"></div>
  <div class="vine" role="img" aria-label="Trailing ivy vine with red berries" style="left:520px;top:10px;width:280px;height:70px"></div>
  <div class="swoosh" role="img" aria-label="Soft rainbow brush swoosh"></div>
  <div class="programme inside-title">The Inner Return</div>

  <p class="copy intro"><b>A</b> Labyrinth is an ancient human symbol for the journey of spiritual awakening. It is not a maze. It has no dead ends, no choices and no corners. As you ‘meander’ you contemplate in silence who and what you ‘really’ are. You review and throw off all the old ideas about your self along the way, while gently realising your true spiritual nature. By the time you reach the centre you have freed your self from all mental illusions and emotional burdens. The authentic and unconditioned self has awoken. You have realised who you really are - the spiritual being animating and playing through a human form. Soul not body! You are able to be your ‘true self’ again. And that changes almost everything!</p>

  <p class="copy lead"><b>As</b> you stop at the six different standing sculptures, contemplate what they mean to you. There is no one right interpretation as we all awaken to who and what we are in our own way. Here is one interpretation reflecting the creators inspirations.</p>

  <div class="entry copy" style="left:48px;top:245px;width:252px">
    <h3>Self AWARENESS</h3>
    <div class="motto">I am. Soul - I am Light - I am Love</div>
    <p>Take a moment to contemplate a different way of ‘seeing’ your self. Take a moment to ‘consider’ your self to be a soul, a spiritual being. Now hold that gently at the back of your awareness as you meander silently to the centre of the Labyrinth.</p>
  </div>
  <div class="rule" style="left:48px;top:323px;width:265px"></div>
  <div class="sculpture" role="img" aria-label="Stone pillar sculpture in a garden" style="left:313px;top:232px;height:103px"></div>

  <div class="sculpture dark" role="img" aria-label="Dark stone pillar sculpture in a garden" style="left:51px;top:329px;height:106px"></div>
  <div class="entry copy" style="left:122px;top:339px;width:248px">
    <h3>Self DISCOVERY</h3>
    <p>Each day there are contrasting and conflicting thoughts and feelings within. Some light and some dark. There is virtue and vice. The virtues of my character are like gold. They are ‘real’ and forever. The vices within my character are like ghosts, dark and temporary.</p>
  </div>
  <div class="rule" style="left:109px;top:425px;width:261px"></div>

  <div class="entry copy" style="left:48px;top:459px;width:252px">
    <h3>Self UNDERSTANDING</h3>
    <p>The reality is that while my thoughts and feelings may change the ‘real’ me cannot change. <b>I will be again what I always was.</b> I am the eternal being. I can only realise this for my self from the inside! (hence the back to front wording on the stone)</p>
  </div>
  <div class="rule" style="left:48px;top:524px;width:265px"></div>
  <div class="sculpture" role="img" aria-label="Stone pillar sculpture in a garden" style="left:313px;top:429px;height:105px"></div>

  <div class="entry copy" style="left:426px;top:197px;width:250px">
    <h3>Self MASTERY</h3>
    <div class="motto">Victory and Faith.</div>
    <p>Each day is filled with victory and defeat. I know defeat when I react emotionally. I know <b>Victory</b> when I consciously respond from a state of inner peace and with love, even when challenged and tested by others. My <b>Faith</b> is sustained when I drink from ‘the inner grail’ in which I can always find my peace and my capacity to love. This is ‘the grail’ of my true nature.</p>
  </div>
  <div class="sculpture" role="img" aria-label="Stone pillar sculpture in a garden" style="left:691px;top:193px;height:104px"></div>

  <div class="sculpture dark" role="img" aria-label="Dark stone pillar sculpture in a garden" style="left:426px;top:312px;height:102px"></div>
  <div class="entry copy" style="left:499px;top:334px;width:245px">
    <h3>Self WORTH</h3>
    <p>I want <b>NOMORE</b>. I crave <b>NOMORE</b>. I need <b>NOMORE.</b> The old me who used to think ‘my wealth was my worth’ is <b>NOMORE</b>. ALL the old me’s have died. I can see the true worth and beauty of the real me starting to grow and blossom.</p>
  </div>
  <div class="rule" style="left:426px;top:407px;width:322px"></div>

  <div class="entry copy" style="left:426px;top:452px;width:250px">
    <h3>Self REALISATION</h3>
    <div class="motto">Om. I am.</div>
    <p>Now I know my self as no one other than the ‘I’ that says, “I am”. This is the true me. Free of all the other false ‘me’s’ I can now walk back into the world as the authentic self and just be... my self!.</p>
  </div>
  <div class="rule" style="left:426px;top:524px;width:265px"></div>
  <div class="sculpture" role="img" aria-label="Stone pillar sculpture in a garden" style="left:691px;top:429px;height:105px"></div>
</section>

</body>
</html>
```